Business card, Invoice and printable service brochure

I need a 5.5x8.5 invoice, business card and printable service template for reception desk designed for my Rug repair, restoration and cleaning business.

I have included a picture for reference

www.kolvenrug.com

Columns i need in my invoice:
Type of rug, Size, Background Color, Repair needs, Notes, Price and rug cleaning disclaimer.

Target Market(s)

Higher segment clients

Industry/Entity Type

Rug Repair, Restoration and cleaning,

Requirements
Must have
• Services hast to be listed on the invoice as well as service brochure.

```html
<!DOCTYPE html>
<html lang="en">
<head>
<meta charset="utf-8">
<title>Kolven Rug – Invoice</title>
<link rel="stylesheet" href="https://fonts.googleapis.com/css2?family=Rajdhani:wght@500;600;700&family=Exo+2:wght@300;400&display=swap">
<style>
  :root {
    --canvas: #e6e6e6;
    --ink: #262626;
    --gold: #a8823f;
    --gold-soft: #b99b58;
    --gold-light: #c6ab68;
    --white: #ffffff;
    --cell-a: #eff0ee;
    --cell-b: #f9f9f8;
    --rule: #d2d3d1;
    --text-dark: #2b2a26;
  }
  * { box-sizing: border-box; margin: 0; padding: 0; }
  html, body { width: 1200px; height: 1000px; overflow: hidden; background: var(--canvas); }
  .invoice {
    position: absolute; left: 261px; top: 20px;
    width: 678px; height: 960px;
    background: var(--ink); overflow: hidden;
    font-family: "Rajdhani", sans-serif; color: var(--white);
    box-shadow: 0 6px 18px rgba(0,0,0,.25);
  }
  .shape { position: absolute; left: 0; top: 0; }
  .brand {
    position: absolute; left: 55px; top: 46px;
    font-family: "Rajdhani", sans-serif; font-weight: 600;
    font-size: 31px; letter-spacing: 1px; color: var(--gold);
  }
  .title {
    position: absolute; left: 384px; top: 24px; width: 256px; text-align: center;
    font-weight: 700; font-size: 50px; letter-spacing: 2px; line-height: 1;
  }
  .bill-to { position: absolute; left: 55px; top: 155px; }
  .bill-to h2 { font-weight: 700; font-size: 19px; color: var(--gold); line-height: 1; }
  .bill-to .client { font-family: "Exo 2", sans-serif; font-weight: 300; font-size: 13px; margin-top: 9px; }
  .bill-to .contact {
    display: flex; align-items: center; gap: 8px;
    font-family: "Exo 2", sans-serif; font-weight: 300; font-size: 11px; margin-top: 4px;
  }
  .bill-to svg { width: 10px; height: 10px; fill: var(--white); }
  .items {
    position: absolute; left: 53px; top: 267px; width: 572px; height: 349px;
    display: grid;
    grid-template-columns: 75px 72px 122px 100px 69px 134px;
    grid-template-rows: 35px 29px 42px 40px 40px 37px 41px 37px 48px;
  }
  .items .head {
    background: var(--gold); color: var(--white);
    padding: 5px 0 0 12px; line-height: 1;
  }
  .items .head small { display: block; font-size: 10px; font-weight: 700; height: 9px; }
  .items .head span { display: block; font-size: 16px; font-weight: 700; }
  .items .cell { border-top: 1px solid var(--rule); }
  .items .cell:nth-child(-n+12) { border-top: none; }
  .items .cell.a { background: var(--cell-a); }
  .items .cell.b { background: var(--cell-b); }
  .services { position: absolute; left: 62px; top: 638px; color: var(--text-dark); }
  .services h3 { font-weight: 700; font-size: 16px; line-height: 1; }
  .services ul { margin-top: 11px; list-style: none; font-family: "Exo 2", sans-serif; font-size: 10.5px; line-height: 13.3px; }
  .services li::before { content: "•"; display: inline-block; width: 22px; padding-left: 4px; font-size: 8px; }
  .totals { position: absolute; left: 438px; top: 639px; width: 189px; font-weight: 700; }
  .totals .row { display: flex; justify-content: space-between; font-size: 11.5px; height: 21px; padding-right: 24px; }
  .totals .grand { border-top: 1px solid var(--white); margin-top: 6px; padding-top: 10px; font-size: 16px; padding-right: 15px; }
  .thanks { position: absolute; left: 62px; top: 804px; font-weight: 700; font-size: 15px; }
  .sign { position: absolute; left: 477px; top: 873px; width: 144px; border-top: 1px solid var(--white);
    text-align: center; font-weight: 700; font-size: 15px; padding-top: 2px; }
</style>
</head>
<body>
<main class="invoice">
  <svg class="shape" width="678" height="960" viewBox="0 0 678 960" aria-hidden="true">
    <defs>
      <linearGradient id="band" x1="0" y1="0" x2="0" y2="1">
        <stop offset="0" stop-color="#b3944f"/>
        <stop offset="1" stop-color="#c6ab68"/>
      </linearGradient>
    </defs>
    <polygon points="384,0 678,0 628,115 334,115" fill="#a8823f"/>
    <polygon points="0,454 53,454 53,616 362,616 284,800 0,800" fill="url(#band)"/>
  </svg>

  <div class="brand">KOLVEN RUG</div>
  <h1 class="title">INVOICE</h1>

  <section class="bill-to">
    <h2>Invoice To:</h2>
    <p class="client">Client Name</p>
    <p class="contact">
      <svg viewBox="0 0 24 24"><path d="M6.6 10.8a15.1 15.1 0 0 0 6.6 6.6l2.2-2.2a1 1 0 0 1 1-.25 11.4 11.4 0 0 0 3.6.57 1 1 0 0 1 1 1V20a1 1 0 0 1-1 1A17 17 0 0 1 3 4a1 1 0 0 1 1-1h3.5a1 1 0 0 1 1 1c0 1.25.2 2.45.57 3.57a1 1 0 0 1-.25 1z"/></svg>
      (555) 014-2297
    </p>
    <p class="contact">
      <svg viewBox="0 0 24 24"><path d="M12 2a7 7 0 0 0-7 7c0 5.25 7 13 7 13s7-7.75 7-13a7 7 0 0 0-7-7zm0 9.5A2.5 2.5 0 1 1 12 6.5a2.5 2.5 0 0 1 0 5z"/></svg>
      1842 Marlow Ave, Brenton, IL 60099
    </p>
  </section>

  <section class="items">
    <div class="head"><small>Type of</small><span>Rug</span></div>
    <div class="head"><small>Background</small><span>Color</span></div>
    <div class="head"><small>Repair</small><span>Needs</span></div>
    <div class="head"><small></small><span>Notes</span></div>
    <div class="head"><small></small><span>Price</span></div>
    <div class="head"><small>Rug cleaning</small><span>Disclaimer</span></div>

    <div class="cell a"></div><div class="cell b"></div><div class="cell a"></div><div class="cell b"></div><div class="cell a"></div><div class="cell b"></div>
    <div class="cell a"></div><div class="cell b"></div><div class="cell a"></div><div class="cell b"></div><div class="cell a"></div><div class="cell b"></div>
    <div class="cell a"></div><div class="cell b"></div><div class="cell a"></div><div class="cell b"></div><div class="cell a"></div><div class="cell b"></div>
    <div class="cell a"></div><div class="cell b"></div><div class="cell a"></div><div class="cell b"></div><div class="cell a"></div><div class="cell b"></div>
    <div class="cell a"></div><div class="cell b"></div><div class="cell a"></div><div class="cell b"></div><div class="cell a"></div><div class="cell b"></div>
    <div class="cell a"></div><div class="cell b"></div><div class="cell a"></div><div class="cell b"></div><div class="cell a"></div><div class="cell b"></div>
    <div class="cell a"></div><div class="cell b"></div><div class="cell a"></div><div class="cell b"></div><div class="cell a"></div><div class="cell b"></div>
    <div class="cell a"></div><div class="cell b"></div><div class="cell a"></div><div class="cell b"></div><div class="cell a"></div><div class="cell b"></div>
  </section>

  <section class="services">
    <h3>Our Services:</h3>
    <ul>
      <li>Rug Repair</li>
      <li>Rug Restoration</li>
      <li>Rug Cleaning</li>
      <li>Rug Installation</li>
      <li>Color Correction</li>
    </ul>
  </section>

  <section class="totals">
    <div class="row"><span>Sub Total:</span><span>$100.00</span></div>
    <div class="row"><span>Tax</span><span>0.00 %</span></div>
    <div class="row grand"><span>Total:</span><span>$100.00</span></div>
  </section>

  <p class="thanks">Thank you for your business</p>
  <p class="sign">Authorised Sign</p>
</main>
</body>
</html>
```